Dorian Walsby Psychotherapy Business Card Design Project

I need a welcoming business card for a Somatic Psychotherapy private practice based in Melbourne, Australia. I help individual clients to work through issues in their life that are inhibiting achieving their full potential. I would like a san serif font and the oculars are:
blue: R:37 G:61 B:95 C:93 M:77 Y:38 K:28
orange: R:241 G:103 B:43 C:0 M:74 Y:93 K:0
The final design should communicate warm, welcoming and safe environment in which clients are supported to grow. It should also convey a collaborative approach to achieve success between me (the therapist) and the client. The uploaded file is my new logo. Also an organic look and feel while maintaining professionalism and a clean, simple look is sought after.
In addition to the logo my details are:
Dorian Walsby
Psychotherapist
B.Arts., Grad Dip. T&D., Dip.Som.Psych, MRKTA, MLOHVB
0417 582 930
dwalsby@dorianwalsby.com.au
www.dorianwalsby.com.au
Target Market(s)
Psychotherapy Clients
Industry/Entity Type
Environment

```html
<!DOCTYPE html>
<html lang="en">
<head>
<meta charset="utf-8">
<title>Dorian Walsby Psychotherapy – Business Card</title>
<link rel="stylesheet" href="https://fonts.googleapis.com/css2?family=Arimo:wght@400;700&display=swap">
<style>
  :root {
    --navy: #253d5f;
    --orange: #f1672b;
    --paper: #f7f8fa;
    --grey-text: #9a9ea5;
    --backdrop: #8c8c8a;
    --white: #ffffff;
  }
  * { margin: 0; padding: 0; box-sizing: border-box; }
  html, body {
    width: 1200px;
    height: 774px;
    overflow: hidden;
    background: var(--backdrop);
    font-family: "Arimo", Arial, sans-serif;
  }
  .stage {
    position: relative;
    width: 1200px;
    height: 774px;
  }
  .card {
    position: absolute;
    top: 238px;
    width: 520px;
    height: 298px;
    border-radius: 3px;
    overflow: hidden;
  }
  /* Front side */
  .card--front {
    left: 60px;
    background: var(--paper);
    color: var(--navy);
  }
  .identity {
    position: absolute;
    top: 26px;
    right: 30px;
    text-align: right;
  }
  .identity__name {
    font-weight: 700;
    font-size: 32px;
    letter-spacing: -0.3px;
    line-height: 1;
  }
  .identity__surname { color: var(--orange); }
  .identity__role {
    font-size: 13px;
    color: var(--grey-text);
    margin-top: 2px;
    margin-right: 18px;
  }
  .credentials {
    position: absolute;
    top: 92px;
    left: 0;
    width: 100%;
    height: 22px;
    background: var(--navy);
    color: var(--white);
    font-size: 13px;
    display: flex;
    align-items: center;
    justify-content: flex-end;
    gap: 10px;
    padding-right: 30px;
  }
  .credentials__sep {
    width: 5px;
    height: 5px;
    border-radius: 50%;
    background: var(--white);
  }
  .contact {
    position: absolute;
    left: 36px;
    top: 170px;
    list-style: none;
  }
  .contact__item {
    display: flex;
    align-items: center;
    gap: 16px;
    font-size: 19px;
    height: 34px;
  }
  .contact__icon {
    width: 22px;
    height: 18px;
    flex: none;
  }
  /* Back side */
  .card--back {
    left: 620px;
    background: var(--navy);
    color: var(--white);
    display: flex;
    align-items: center;
    justify-content: center;
    gap: 16px;
  }
  .brand__mark {
    width: 46px;
    height: 46px;
    border-radius: 50%;
    background: var(--white);
    flex: none;
  }
  .brand__name {
    font-weight: 700;
    font-size: 30px;
    line-height: 1.1;
    letter-spacing: 0.2px;
  }
</style>
</head>
<body>
<main class="stage">
  <section class="card card--front" aria-label="Business card front">
    <div class="identity">
      <p class="identity__name">Dorian <span class="identity__surname">Walsby</span></p>
      <p class="identity__role">Psychotherapist</p>
    </div>
    <div class="credentials">
      <span>B.Arts.</span><span class="credentials__sep"></span>
      <span>Grad Dip. T&amp;D</span><span class="credentials__sep"></span>
      <span>Dip.Som.Psych.</span><span class="credentials__sep"></span>
      <span>MRKTA</span><span class="credentials__sep"></span>
      <span>MLOHVB</span>
    </div>
    <ul class="contact">
      <li class="contact__item">
        <svg class="contact__icon" viewBox="0 0 22 18" aria-hidden="true">
          <rect x="1" y="4" width="20" height="13" rx="2" fill="#f1672b"/>
          <rect x="3" y="1" width="16" height="5" rx="2" fill="#f1672b"/>
          <g fill="#f7f8fa">
            <rect x="5" y="8" width="3" height="2"/><rect x="10" y="8" width="3" height="2"/><rect x="15" y="8" width="3" height="2"/>
            <rect x="5" y="12" width="3" height="2"/><rect x="10" y="12" width="3" height="2"/><rect x="15" y="12" width="3" height="2"/>
          </g>
        </svg>
        <span>0417 582 930</span>
      </li>
      <li class="contact__item">
        <svg class="contact__icon" viewBox="0 0 22 18" aria-hidden="true">
          <rect x="1" y="2" width="20" height="14" rx="1.5" fill="#f1672b"/>
          <polyline points="2,3 11,10 20,3" fill="none" stroke="#f7f8fa" stroke-width="1.6"/>
        </svg>
        <span>dwalsby@dorianwalsby.com.au</span>
      </li>
      <li class="contact__item">
        <svg class="contact__icon" viewBox="0 0 22 18" aria-hidden="true">
          <g fill="#f1672b">
            <rect x="1" y="3" width="3" height="13"/><rect x="6" y="6" width="3" height="10"/>
            <rect x="11" y="9" width="3" height="7"/><rect x="16" y="12" width="3" height="4"/>
            <rect x="1" y="16" width="20" height="1.5"/>
          </g>
        </svg>
        <span>www.dorianwalsby.com.au</span>
      </li>
    </ul>
  </section>

  <section class="card card--back" aria-label="Business card back">
    <span class="brand__mark" aria-hidden="true"></span>
    <p class="brand__name">Dorian Walsby<br>Psychotherapy</p>
  </section>
</main>
</body>
</html>
```